Morvella- providing risk management solutions to the cannabis industry, including track&trace,

need graphics for a tradeshow booth 10x10 (the front and right side of booth will be open) 1 large graphic for the back (like shown on your example). Will need 2 pop up standing graphics (also like shown in your example). name of company is Morvella (description/brief is included file 3)
We will be promoting software and anti-counterfeit packaging solutions for the cannabis industry. One of the pop-ups may contain actual industry published headlines (see file 2 attached) that illustrate the need for these risk management solutions.
Updates

some designs did not follow request in brief, some designs were duplicates, overall quality is disappointing.

I am hoping that more designers will look at this initial project- not sure if you realize this reflects an industry (legalized cannabis in USA) that is expected to grow (no pun intended) by more than 80% in the next 3 years with revenues topping more than $30billion USD. Any projects that show experience in this field are likely to get noticed and be good future focus for your business. (assuming that this industry is not something you conscientiously object to, however if this is the case, totally understand)

Target Market(s)

Cannabis industry: Growers- Extractors- Edibles and other manufacturers using Cannabis as ingredient. providing B2B solutions not directed to consumer, and we are considered an ancillary industry supplier (don't touch product)

Font styles to use
Serif

Colors

Requirements
Must have
• professional software and risk management solutions feel, this is an industry that is coming out of the "out past dusk" van to a very legitimate business that will require the same protocols and systems as pharma and food safety.
Nice to have
• the industry wants to be viewed as "mainstream and legitimate" especially when it comes to business risk mitigation (which is important to business owners and investors). we are providing solutions track/trace, anti-counterfeit, supply chain integrity in some cases where industry has not yet experienced the issue or not yet mandated by regulatory body....but its coming. ( we say: todays solutions for tomorrow's challenges)
Should not have
• catchy cannabis slogans....weed, ganja, stoned...etc.

```html
<!DOCTYPE html>
<html lang="en">
<head>
<meta charset="utf-8">
<title>Morvella – Tradeshow Backdrop</title>
<link href="https://fonts.googleapis.com/css2?family=Oswald:wght@400;500;600&family=Montserrat:wght@800&family=Raleway:wght@400&display=swap" rel="stylesheet">
<style>
  :root {
    --page-bg: #e8e8e8;
    --panel-bg: #ffffff;
    --brand-blue: #2f7bd6;
    --brand-blue-deep: #1d5fb8;
    --ink: #111111;
    --photo-dark: #5a4a3a;
    --photo-light: #c9a48d;
    --leaf-green: #7c8a45;
    --leaf-light: #c9c98a;
  }
  * { box-sizing: border-box; margin: 0; padding: 0; }
  html, body { width: 1200px; height: 929px; overflow: hidden; background: var(--page-bg); }
  .backdrop {
    position: absolute; left: 150px; top: 7px;
    width: 900px; height: 915px;
    background: var(--panel-bg);
    overflow: hidden;
  }
  .backdrop-art { position: absolute; inset: 0; width: 900px; height: 915px; }
  .tagline {
    position: absolute; left: 0; width: 900px; text-align: center; white-space: nowrap;
    line-height: 1;
  }
  .tagline-main {
    top: 460px;
    font-family: "Oswald", sans-serif; font-weight: 500;
    font-size: 86px; color: var(--ink); letter-spacing: 1px;
  }
  .tagline-sub {
    top: 566px;
    font-family: "Montserrat", sans-serif; font-weight: 800;
    font-size: 50px; color: var(--brand-blue); letter-spacing: 1px;
  }
  .headline-box {
    position: absolute; left: 17px; top: 632px; width: 867px; height: 158px;
    border: 1.5px solid var(--brand-blue);
    display: flex; flex-direction: column; justify-content: center; align-items: center;
    gap: 8px;
  }
  .headline {
    font-family: "Oswald", sans-serif; white-space: nowrap; line-height: 1.1;
    text-transform: uppercase;
  }
  .headline-plain { font-weight: 400; font-size: 24px; color: var(--ink); }
  .headline-feature { font-weight: 600; font-size: 31px; color: var(--brand-blue); }
  .headline-small { font-size: 23px; }
  .brand-name {
    position: absolute; left: 155px; top: 822px;
    font-family: "Raleway", sans-serif; font-weight: 400;
    font-size: 46px; letter-spacing: 3px; color: var(--ink);
  }
</style>
</head>
<body>
<main class="backdrop">
  <svg class="backdrop-art" viewBox="0 0 900 915">
    <defs>
      <linearGradient id="photoTone" x1="0" y1="0" x2="1" y2="1">
        <stop offset="0" stop-color="#d8b5a0"/>
        <stop offset="0.35" stop-color="#7c8a45"/>
        <stop offset="0.7" stop-color="#5a4a3a"/>
        <stop offset="1" stop-color="#c9a48d"/>
      </linearGradient>
      <radialGradient id="budTone" cx="0.5" cy="0.5" r="0.6">
        <stop offset="0" stop-color="#c9c98a"/>
        <stop offset="0.6" stop-color="#7c8a45"/>
        <stop offset="1" stop-color="#3f4a22"/>
      </radialGradient>
      <radialGradient id="candyTone" cx="0.55" cy="0.45" r="0.55">
        <stop offset="0" stop-color="#e3d65a" stop-opacity="0.9"/>
        <stop offset="0.5" stop-color="#e8894a" stop-opacity="0.55"/>
        <stop offset="1" stop-color="#ffffff" stop-opacity="0"/>
      </radialGradient>
    </defs>

    <path class="hero-photo" role="img" aria-label="Close-up photo of a cured plant flower held in an open hand"
          fill="url(#photoTone)"
          d="M0 0 H880 C770 50 680 130 600 190 L520 400 C380 440 180 420 0 310 Z"/>

    <path class="band-top-line" fill="#111111"
          d="M640 178 C730 100 810 45 900 12 V34 C815 62 735 120 650 190 Z"/>
    <path class="band-top" fill="#2f7bd6"
          d="M660 190 C740 120 820 62 900 30 V72 C820 95 745 140 672 200 Z"/>

    <path class="band-left-line" fill="#111111"
          d="M0 345 C170 452 380 470 530 420 L536 432 C380 490 160 470 0 362 Z"/>
    <path class="band-left" fill="#2f7bd6"
          d="M0 310 C180 420 380 440 520 400 L530 420 C380 470 170 452 0 345 Z"/>

    <rect class="candy-photo" role="img" aria-label="Photo of wrapped hard candies spilling from a glass jar"
          x="640" y="110" width="260" height="340" rx="120" fill="url(#candyTone)"/>

    <circle class="plant-photo" role="img" aria-label="Photo of a flowering plant top seen from above"
            cx="532" cy="286" r="131" fill="url(#budTone)" stroke="#2f7bd6" stroke-width="7"/>

    <path class="band-bottom" fill="#2f7bd6"
          d="M440 915 C600 868 720 818 900 800 V915 Z"/>
    <path class="band-bottom-line" fill="none" stroke="#111111" stroke-width="7"
          d="M440 915 C600 868 720 818 900 800"/>
  </svg>

  <h1 class="tagline tagline-main">TODAYS SOLUTIONS FOR</h1>
  <h2 class="tagline tagline-sub">TOMORROW'S CHALLENGES</h2>

  <section class="headline-box">
    <p class="headline headline-plain">"5th grader unknowingly passes out pot edibles to schoolmates" Jan 17 2018</p>
    <p class="headline headline-feature">"The cannabis counterfeit battle has begun" April 17, 2017</p>
    <p class="headline headline-plain headline-small">"California marijuana labeling snafu leads to yet another recall" August 15, 2018</p>
  </section>

  <div class="brand-name">MORVELLA</div>
</main>
</body>
</html>
```